New business card for civil engineering company - "Keystone Audit"

We need a business card designed for our new structural engineering company.

The company name is "Keystone Audit" logo files attached.

We would like the following:
* Two-sided card
* Simple design

Information to be placed on the card:
Name - Marcus Dellow
Job Title - Director / Structural Engineer
Credentials - BEng(Hons), CPEng, CMengNZ, IntPE(NZ)
Email - marcus.dellow@keystoneaudit.co.nz
mobile - 0219364058
website - www.keystoneaudit.co.nz

```html
<!DOCTYPE html>
<html lang="en">
<head>
<meta charset="utf-8">
<title>Keystone Audit – Business Card</title>
<link href="https://fonts.googleapis.com/css2?family=Lato:wght@400;700&display=swap" rel="stylesheet">
<style>
  :root {
    --backdrop: #b9bbbe;
    --navy: #0b4274;
    --navy-light: #1a5a92;
    --brand-blue: #1f7fd0;
    --rule-blue: #5aa6e6;
    --ink: #3a3d42;
    --brand-ink: #3d4147;
    --paper: #ffffff;
  }
  * { box-sizing: border-box; margin: 0; padding: 0; }
  html, body {
    width: 1200px; height: 930px; overflow: hidden;
    background: var(--backdrop);
    font-family: "Lato", sans-serif;
  }
  .sheet {
    width: 1200px; height: 930px;
    display: flex; flex-direction: column; align-items: center; justify-content: center;
    gap: 30px;
  }
  .card {
    width: 687px; height: 420px;
    border-radius: 26px;
    position: relative;
    overflow: hidden;
    box-shadow: 0 6px 18px rgba(0,0,0,0.18);
  }
  /* Front */
  .card--front {
    background: linear-gradient(100deg, var(--navy-light) 0%, var(--navy) 45%, var(--navy) 100%);
    display: flex; align-items: center; justify-content: center;
  }
  .brand {
    display: flex; align-items: center; gap: 14px;
    font-weight: 700; letter-spacing: 0.04em; text-transform: uppercase;
  }
  .brand__square { width: 22px; height: 22px; background: var(--brand-blue); }
  .card--front .brand { color: var(--paper); font-size: 34px; }
  .card--front .brand__square { background: #4fa3e8; }
  /* Back */
  .card--back {
    background: var(--paper);
    display: flex; align-items: center;
  }
  .back__brand-zone {
    width: 300px; height: 100%;
    display: flex; align-items: center; justify-content: center;
  }
  .card--back .brand { color: var(--brand-ink); font-size: 24px; gap: 10px; }
  .back__rule {
    width: 1.5px; height: 190px; background: var(--rule-blue);
  }
  .contact { padding-left: 40px; color: var(--ink); }
  .contact__name {
    color: var(--brand-blue); font-size: 32px; font-weight: 400;
    text-transform: uppercase; letter-spacing: 0.01em; line-height: 1.1;
  }
  .contact__role { font-size: 18px; line-height: 1.3; margin-top: 4px; }
  .contact__list { list-style: none; margin-top: 14px; font-size: 18px; line-height: 1.45; }
  .contact__list li { display: flex; align-items: center; gap: 10px; }
  .contact__list svg { width: 14px; height: 14px; flex: none; }
</style>
</head>
<body>
  <main class="sheet">
    <section class="card card--front" aria-label="Card front">
      <div class="brand"><span class="brand__square"></span>Keystone Audit</div>
    </section>

    <section class="card card--back" aria-label="Card back">
      <div class="back__brand-zone">
        <div class="brand"><span class="brand__square"></span>Keystone Audit</div>
      </div>
      <div class="back__rule"></div>
      <div class="contact">
        <h1 class="contact__name">Marcus Dellow</h1>
        <p class="contact__role">Director / Structural Engineer<br>BEng(Hons), CPEng,<br>CMengNZ, IntPE(NZ)</p>
        <ul class="contact__list">
          <li>
            <svg viewBox="0 0 16 16" aria-hidden="true"><path fill="#1f7fd0" d="M3.6 1.5l2.3 2.6-1.3 1.7c.9 2 2.4 3.6 4.5 4.6l1.7-1.3 2.7 2.2-1.3 2.3C6.6 14.8 1.2 9.4 1.4 3z"/></svg>
            0219364058
          </li>
          <li>
            <svg viewBox="0 0 16 16" aria-hidden="true"><rect x="1.5" y="3.5" width="13" height="9" fill="none" stroke="#1f7fd0" stroke-width="1.6"/><path d="M1.5 3.5l6.5 5 6.5-5" fill="none" stroke="#1f7fd0" stroke-width="1.6"/></svg>
            marcus.dellow@keystoneaudit.co.nz
          </li>
          <li>
            <svg viewBox="0 0 16 16" aria-hidden="true"><g fill="none" stroke="#1f7fd0" stroke-width="1.3"><circle cx="8" cy="8" r="6.3"/><ellipse cx="8" cy="8" rx="2.8" ry="6.3"/><path d="M1.7 8h12.6M2.8 4.8h10.4M2.8 11.2h10.4"/></g></svg>
            www.keystoneaudit.co.nz
          </li>
        </ul>
      </div>
    </section>
  </main>
</body>
</html>
```